Postcard design for accounting company

We need a postcard design (front and back) to our accounting firm that provides bookkeeping services to small and mid-size companies using TallyHive Online. We would like to see designs that use the color blue and match our overall branding (see website). The final design should communicate professionalism, trust, and ease.

Target Market(s)

Small and Mid-Size companies

Industry/Entity Type

Accounting

Colors
0054AA
0677BA
7BADD7
CADEEF
E8F1F8

Requirements
Must have
• Logo, contact information, indicate services offered, color blue, and fit postcard template (see attached). Contact info = 555.203.8841, 1.800.555.0142, Info@FernwayAccounting.example, www.FernwayAccounting.example. Use the PLMX Retail Indicia, which is a postage payment mark that takes the place of a regular postage stamp or meter stamp. Every PLMX mailpiece must include the PLMX Retail Indicia above and to the right of the address block. The PLMX Retail Indicia does not have a specific size requirement but must be larger than 0.5" x 0.5". The type font must be in all caps and at least a 4 point size. It should fit in the area 1.625" from the right edge and 1.375" from top edge. Leave 1/8" of space around the top and right edge. See attached sample.
Nice to have
• Include that we a re Certified TallyHive CertiGuides (can include THO logo). Also, maybe include the logos of the associations we are members of (Pine Hollow Chamber of Commerce, Continental Guild of Certified Ledgerkeepers, and Federated League of Female Enterprise Founders.

```html
<!DOCTYPE html>
<html lang="en">
<head>
<meta charset="utf-8">
<title>Fernway Accounting Postcard</title>
<link href="https://fonts.googleapis.com/css2?family=Montserrat:wght@500;600;700;800;900&family=Roboto+Condensed:wght@400;700&family=Arimo:wght@700&display=swap" rel="stylesheet">
<style>
:root{
  --navy:#16366a;
  --navy-deep:#0f2b57;
  --cyan:#17b2d3;
  --cyan-soft:#bfe6f1;
  --ice:#e8f1f8;
  --grey:#8d8f92;
  --ink:#2b2b2b;
  --white:#ffffff;
  --page:#efedea;
}
*{margin:0;padding:0;box-sizing:border-box}
html,body{width:705px;height:1200px;overflow:hidden;background:var(--page)}
body{position:relative;font-family:"Montserrat",sans-serif;color:var(--ink)}
.card{position:absolute;left:20px;width:665px;height:448px;background:var(--white);overflow:hidden;box-shadow:0 3px 8px rgba(0,0,0,.25)}
.card--front{top:110px}
.card--back{top:642px}
.abs{position:absolute}

/* brand */
.brand{display:flex;align-items:center;gap:8px;color:var(--navy);font-weight:800}
.brand__dot{background:var(--navy);border-radius:50%;flex:none}

/* front */
.front__logo{left:26px;top:38px}
.front__logo .brand__dot{width:26px;height:26px}
.front__logo .brand__name{font-size:24px;line-height:1.05}
.hero{left:0;top:111px;width:292px;height:127px;background:var(--cyan);color:var(--white);padding:14px 0 0 15px}
.hero__title{font-weight:900;font-size:24px;line-height:1.02;letter-spacing:.2px}
.hero__sub{margin-top:10px;border-left:2px solid var(--white);padding-left:7px;font-weight:600;font-size:9.6px;line-height:1.28;width:255px}
.photo{left:298px;top:0;width:367px;height:300px;background:linear-gradient(135deg,#8a6b52 0%,#5c4a3d 45%,#2e3e55 100%);clip-path:polygon(0 0,100% 0,100% 100%,0 82%)}
.photo-edge{left:292px;top:0;width:6px;height:238px;background:var(--cyan)}
.services-bar{left:0;top:238px;width:440px;height:35px}
.services-bar__text{left:15px;top:244px;font-size:18px;font-weight:600;color:var(--white);letter-spacing:.3px}
.services-bar__text b{color:var(--cyan);font-weight:700}
.service{left:15px;width:320px;display:flex;gap:9px}
.service__icon{width:20px;height:22px;flex:none;margin-top:2px}
.service__title{font-size:13px;font-weight:700;color:var(--cyan);line-height:1.1}
.service__text{font-family:"Roboto Condensed",sans-serif;font-size:7.6px;line-height:1.42;color:#333;margin-top:1px}
.contact{left:343px;top:302px;width:185px}
.contact__local{display:inline-block;background:var(--grey);color:var(--white);font-size:13px;font-weight:600;padding:1px 5px;position:relative}
.contact__local::after{content:"";position:absolute;right:-8px;top:0;border-left:8px solid var(--grey);border-top:9px solid transparent;border-bottom:9px solid transparent}
.contact__toll{display:flex;align-items:center;gap:4px;color:var(--cyan);font-weight:800;font-size:17.5px;margin-top:2px}
.contact__row{display:flex;align-items:center;gap:5px;font-size:7.8px;color:var(--grey);margin-top:1px}
.contact__web{display:flex;align-items:center;gap:5px;background:var(--cyan);color:var(--white);font-weight:700;font-size:7.8px;padding:3px 4px;margin-top:3px;width:190px}
.contact__assoc{font-size:6.3px;color:var(--navy);margin-top:5px;border-bottom:1px solid var(--cyan);padding-bottom:2px;width:230px}
.badges{display:flex;gap:12px}
.badge{width:33px;height:33px;border-radius:50%;border:2px solid #d8cfa6;background:#f4efdc}
.badge--green{background:#dfece1;border-color:#b7cbb8}
.badge--ring{background:#fbf6e8;border-color:#e2c27a}
.laptop{left:498px;top:292px;width:150px;height:133px;background:linear-gradient(180deg,#cfd6de,#8b96a3);border-radius:4px}

/* back */
.pack-panel{left:0;top:0;width:370px;height:323px;background:linear-gradient(160deg,var(--navy) 0%,var(--navy-deep) 100%);border-left:6px solid var(--cyan)}
.pack-head{left:22px;top:14px;width:318px;height:29px;border:1px solid #6d85a8;display:flex;align-items:center;gap:10px;padding-left:10px}
.pack-head__icon{width:16px;height:16px}
.pack-head__text{font-size:18px;color:var(--cyan);font-weight:500;letter-spacing:.5px}
.pack-head__text b{color:var(--white);font-weight:800}
.tier{width:100px;text-align:center;color:var(--white)}
.tier__img{width:86px;height:50px;margin:0 auto;background:linear-gradient(180deg,#9cc9e6,#3f79a8)}
.tier__label{background:var(--cyan);font-weight:700;font-size:10px;letter-spacing:.8px;padding:2px 0;margin:0 4px;clip-path:polygon(0 0,100% 0,94% 100%,6% 100%);color:var(--navy-deep)}
.tier__text{font-family:"Roboto Condensed",sans-serif;font-size:7.4px;line-height:1.45;margin-top:3px}
.tier__note{font-family:"Roboto Condensed",sans-serif;font-size:5px;border:1px solid var(--cyan);margin:5px 2px 0;padding:1px 0}
.pledge{left:22px;top:190px;width:240px;border-left:2px solid var(--cyan);padding-left:8px;color:var(--white);font-size:8.6px;font-weight:500;line-height:1.35}
.svc-head{left:22px;top:234px;width:270px;height:19px;background:var(--white);clip-path:polygon(0 0,100% 0,94% 100%,0 100%);padding-left:10px;font-size:11px;font-weight:700;color:var(--cyan);line-height:19px}
.svc-head b{color:var(--navy)}
.svc-box{left:22px;top:253px;width:240px;height:66px;background:var(--grey);clip-path:polygon(0 0,100% 0,94% 100%,0 100%);display:flex;padding:4px 0 0 10px;color:var(--white);font-size:6.7px;font-weight:700;line-height:1.55}
.svc-box ul{list-style:none;width:112px}
.svc-box li::before{content:"\2713";margin-right:4px}
.back-contact{left:22px;top:327px;width:240px}
.back-contact__phones{display:flex;gap:4px}
.phone-chip{display:flex;align-items:center;gap:3px;font-size:11.5px;font-weight:600;padding:1px 4px}
.phone-chip--grey{background:var(--grey);color:var(--white)}
.phone-chip--navy{background:var(--navy);color:var(--white)}
.back-contact .contact__row{font-size:9px;margin-top:3px}
.back-contact .contact__web{font-size:9px;width:220px;margin-top:3px}
.back-assoc{left:22px;top:393px;display:flex;align-items:center;gap:10px}
.back-assoc__label{font-size:6.5px;color:var(--navy);line-height:1.15;border-right:1px solid var(--cyan);padding-right:10px}
.device{left:238px;top:183px;width:150px;height:226px;background:linear-gradient(160deg,#f1f3f4 0%,#c6ccd1 60%,#6aba3a 100%);border-radius:18px;transform:rotate(8deg)}
.stripe{left:10px;top:432px;width:655px;height:16px;background:var(--cyan);clip-path:polygon(0 0,98% 0,100% 100%,0 100%)}
.back__logo{left:401px;top:58px}
.back__logo .brand__dot{width:13px;height:13px}
.back__logo .brand__name{font-size:11.5px}
.indicia{left:523px;top:23px;width:120px;height:90px;border:1px solid #555;font-family:"Arimo",sans-serif;font-weight:700;text-align:center;font-size:12px;line-height:1.27;padding-top:6px;color:#111}
.indicia .big{font-size:14px}
.addr-line{height:1px;background:#777}
</style>
</head>
<body>

<!-- FRONT -->
<section class="card card--front" aria-label="Postcard front">
  <div class="abs front__logo brand"><span class="brand__dot"></span><span class="brand__name">Fernway<br>Accounting</span></div>
  <div class="abs photo-edge"></div>
  <div class="abs photo" role="img" aria-label="Photo of hands typing on a laptop showing accounting dashboard on a wooden desk"></div>
  <div class="abs hero">
    <h1 class="hero__title">ACCOUNTING FOR<br>YOUR BUSINESS</h1>
    <p class="hero__sub">Specializing in Cloud-Based Bookkeeping &amp; Payroll Processing with TallyHive Online by Hiveworks.</p>
  </div>
  <svg class="abs services-bar" viewBox="0 0 440 35" aria-hidden="true">
    <polygon points="0,0 440,0 440,35 0,35" fill="#e8f1f8"/>
    <polygon points="0,0 236,0 212,35 0,35" fill="#16366a"/>
    <polygon points="236,0 440,0 440,12 222,20" fill="#bfe6f1"/>
  </svg>
  <div class="abs services-bar__text"><b>SERVICES</b> OFFERED</div>

  <div class="abs service" style="top:285px">
    <svg class="service__icon" viewBox="0 0 20 22" aria-hidden="true"><rect x="3" y="2" width="13" height="17" fill="none" stroke="#8d8f92" stroke-width="1.6"/><path d="M6 7h7M6 11h7M6 15h4" stroke="#8d8f92" stroke-width="1.4"/></svg>
    <div>
      <h2 class="service__title">BOOKKEEPING</h2>
      <p class="service__text">Let us take over the day to day bookkeeping so you can get back to running your business.<br>We offer TallyHive Online setup &amp; ongoing bookkeeping, including daily journal entries, accounts payables &amp; receivables, bill pay, sales tax reporting &amp; payments, account reconciliation, and more.</p>
    </div>
  </div>
  <div class="abs service" style="top:340px">
    <svg class="service__icon" viewBox="0 0 20 22" aria-hidden="true"><rect x="2" y="3" width="10" height="16" fill="none" stroke="#8d8f92" stroke-width="1.6"/><rect x="12" y="9" width="6" height="10" fill="#8d8f92"/><path d="M4 8h6M4 12h6" stroke="#8d8f92" stroke-width="1.3"/></svg>
    <div>
      <h2 class="service__title">FINANCIAL REPORTING</h2>
      <p class="service__text">We'll provide easy to understand financial reports that allow you and your team to manage cash flow, create budgets and make forecasting decisions. Want real time data? Let us provide solutions with the latest in mobile apps and dashboards.</p>
    </div>
  </div>
  <div class="abs service" style="top:394px">
    <svg class="service__icon" viewBox="0 0 20 22" aria-hidden="true"><circle cx="6" cy="6" r="3" fill="#8d8f92"/><circle cx="14" cy="8" r="2.6" fill="#8d8f92"/><rect x="3" y="10" width="6" height="10" fill="#8d8f92"/><rect x="11.5" y="12" width="5" height="8" fill="#8d8f92"/></svg>
    <div>
      <h2 class="service__title">PAYROLL PROCESSING</h2>
      <p class="service__text">Whether you have 5 employees or 100+, payroll can be an overwhelming and time consuming task. We offer full service payroll processing, including employee onboarding and reporting.</p>
    </div>
  </div>

  <div class="abs laptop" role="img" aria-label="Laptop showing bookkeeping software dashboard"></div>
  <div class="abs contact">
    <span class="contact__local">555.203.8841</span>
    <div class="contact__toll">
      <svg width="13" height="13" viewBox="0 0 14 14" aria-hidden="true"><rect x="0.5" y="0.5" width="13" height="13" rx="3" fill="#8d8f92"/><path d="M4 3.5c0 4 2.5 6.5 6.5 6.5l.5-1.8-2-1-1 1c-1-.5-1.7-1.2-2.2-2.2l1-1-1-2z" fill="#fff"/></svg>
      1.800.555.0142
    </div>
    <div class="contact__row"><svg width="9" height="7" viewBox="0 0 9 7" aria-hidden="true"><rect width="9" height="7" fill="#8d8f92"/><path d="M0 0l4.5 4L9 0" stroke="#fff" fill="none"/></svg>Info@FernwayAccounting.example</div>
    <div class="contact__web"><svg width="9" height="9" viewBox="0 0 10 10" aria-hidden="true"><circle cx="5" cy="5" r="4.3" fill="none" stroke="#fff"/><path d="M.7 5h8.6M5 .7v8.6" stroke="#fff" stroke-width=".8"/></svg>www.FernwayAccounting.example</div>
    <div class="contact__assoc">Associations we are members of</div>
    <div class="badges" style="margin-top:6px">
      <span class="badge badge--green"></span><span class="badge" style="background:#eef2f1;border-color:#cdd6d4"></span><span class="badge badge--ring"></span>
    </div>
  </div>
</section>

<!-- BACK -->
<section class="card card--back" aria-label="Postcard back">
  <div class="abs pack-panel"></div>
  <div class="abs pack-head">
    <svg class="pack-head__icon" viewBox="0 0 16 16" aria-hidden="true"><rect x="2" y="2" width="12" height="12" fill="none" stroke="#8d8f92" stroke-width="1.5"/><path d="M5 6h6M5 9h6M5 12h3" stroke="#8d8f92"/></svg>
    <span class="pack-head__text">BOOKKEEPING <b>PACKAGES</b></span>
  </div>
  <div class="abs tier" style="left:24px;top:51px">
    <div class="tier__img" role="img" aria-label="Sailboat on a harbour"></div>
    <div class="tier__label">STARTER</div>
    <p class="tier__text">Bookkeeping for businesses<br>with monthly expenses<br>under $25k</p>
    <p class="tier__note">*transaction volume not to exceed 100/mo</p>
  </div>
  <div class="abs tier" style="left:137px;top:51px">
    <div class="tier__img" role="img" aria-label="Resort infinity pool overlooking the sea"></div>
    <div class="tier__label">MID-LEVEL</div>
    <p class="tier__text">Bookkeeping for businesses<br>with monthly expenses<br>under $50k</p>
    <p class="tier__note">*transaction volume not to exceed 250/mo</p>
  </div>
  <div class="abs tier" style="left:250px;top:51px">
    <div class="tier__img" role="img" aria-label="White seaside village on a hillside"></div>
    <div class="tier__label">EXECUTIVE</div>
    <p class="tier__text">Bookkeeping for businesses<br>with monthly expenses<br>over $50k</p>
    <p class="tier__note">*transaction volume over 250/mo</p>
  </div>
  <p class="abs pledge">Our Certified TallyHive CertiGuides have the Knowledge and Expertise to Ensure Professional, Accurate, High Quality Service.</p>
  <div class="abs svc-head">BOOKKEEPING PACKAGES <b>SERVICES</b></div>
  <div class="abs svc-box">
    <ul><li>Accounts Receivable</li><li>Accounts Payable</li><li>Inventory</li><li>Payroll</li><li>Accruals/Adjusting Entries</li></ul>
    <ul><li>Account Reconciliation</li><li>Financial Reporting</li><li>Sales Tax</li><li>Consulting</li></ul>
  </div>
  <div class="abs back-contact">
    <div class="back-contact__phones">
      <span class="phone-chip phone-chip--grey">555.203.8841</span>
      <span class="phone-chip phone-chip--navy">1.800.555.0142</span>
    </div>
    <div class="contact__row"><svg width="10" height="8" viewBox="0 0 9 7" aria-hidden="true"><rect width="9" height="7" fill="#8d8f92"/><path d="M0 0l4.5 4L9 0" stroke="#fff" fill="none"/></svg>Info@FernwayAccounting.example</div>
    <div class="contact__web"><svg width="10" height="10" viewBox="0 0 10 10" aria-hidden="true"><circle cx="5" cy="5" r="4.3" fill="none" stroke="#fff"/><path d="M.7 5h8.6M5 .7v8.6" stroke="#fff" stroke-width=".8"/></svg>www.FernwayAccounting.example</div>
  </div>
  <div class="abs back-assoc">
    <span class="back-assoc__label">ASSOCIATIONS<br>WE ARE<br>MEMBERS OF</span>
    <div class="badges" style="gap:10px"><span class="badge badge--green"></span><span class="badge" style="background:#eef2f1;border-color:#cdd6d4"></span><span class="badge badge--ring"></span></div>
  </div>
  <div class="abs device" role="img" aria-label="Smartphone on a stand showing certified advisor badge"></div>
  <div class="abs stripe"></div>

  <div class="abs back__logo brand"><span class="brand__dot"></span><span class="brand__name">Fernway<br>Accounting</span></div>
  <div class="abs indicia">PRSRT STD<br>ECRWSS<br>U.S.POSTAGE<br><span class="big">PAID</span><br>PLMX Retail</div>
  <div class="abs addr-line" style="left:393px;top:296px;width:250px"></div>
  <div class="abs addr-line" style="left:393px;top:331px;width:250px"></div>
  <div class="abs addr-line" style="left:397px;top:366px;width:250px"></div>
</section>

</body>
</html>
```